VIP Card Design Project

Trodza is a premium sneaker store selling brand name sneakers like Velm, Quorra, Brenvo and etc. ( www.trodzashop.com ) We need to design a VIP card to promote one of our discount program called "Trodza VIP Circle 9", which offers 24% discount off all full-priced items. The idea is because we have a "Pelmor fitness center" (pelmorfitness.com) next door and we are trying to design a discount program for people going to the fitness center.
The design is for the front of the card. The back will be black and white with benefits information and member information.
The front design need to include our logo, "VIP", "Circle 9" and our web address "Trodza.com" and Chatterly and blipster logo.
It will be a plastic card in the size of 3.375x2.125 (bleed size 3.5x2.25)

```html
<!DOCTYPE html>
<html lang="en">
<head>
<meta charset="utf-8">
<title>Trodza VIP Circle 9 Card</title>
<link rel="stylesheet" href="https://fonts.googleapis.com/css2?family=Luckiest+Guy&family=PT+Sans:wght@400;700&display=swap">
<style>
  :root {
    --green-dark: #1f6b2a;
    --green-mid: #2e8b37;
    --green-bright: #4cb848;
    --orange: #f28a1e;
    --yellow: #f4e51c;
    --white: #ffffff;
    --ink: #1a1a1a;
    --navy: #1d3f7a;
    --stage: #ece9e4;
    --shoe-light: #d9dcdf;
    --shoe-dark: #3a3a2c;
  }
  * { margin: 0; padding: 0; box-sizing: border-box; }
  html, body { width: 1200px; height: 1171px; overflow: hidden; }
  body { background: var(--stage); position: relative; font-family: "PT Sans", Arial, sans-serif; }

  .card {
    position: absolute;
    width: 810px;
    height: 509px;
    border-radius: 28px;
    overflow: hidden;
    background: var(--white);
    box-shadow: 0 6px 18px rgba(0,0,0,0.18);
  }
  .card-front { left: 208px; top: 50px; }
  .card-back { left: 212px; top: 612px; }
  .card-art { position: absolute; inset: 0; }

  .brand-name {
    position: absolute;
    left: 0; right: 0; top: 92px;
    text-align: center;
    font-family: "Luckiest Guy", "Arial Black", sans-serif;
    font-size: 128px;
    line-height: 1;
    color: var(--green-bright);
    letter-spacing: 2px;
  }

  .discount-badge {
    position: absolute;
    width: 54px; height: 54px;
    border-radius: 50%;
    background: var(--green-dark);
    border: 4px solid var(--orange);
    color: var(--white);
    text-align: center;
    font-weight: 700;
    line-height: 1;
    padding-top: 9px;
  }
  .discount-badge .pct { display: block; font-size: 16px; }
  .discount-badge .word { display: block; font-size: 9px; margin-top: 1px; }

  .shoe-photo {
    position: absolute;
    border: 3px solid var(--green-mid);
    border-radius: 24px;
  }
  .shoe-photo.light { background: linear-gradient(160deg, #eef0f2, var(--shoe-light) 55%, #8a7a66); }
  .shoe-photo.dark { background: linear-gradient(160deg, #f4f4f2, var(--shoe-dark) 60%, #e0c21a); }

  .club-title {
    position: absolute;
    left: 0; right: 0; top: 424px;
    text-align: center;
    font-size: 30px;
    font-weight: 700;
    color: var(--yellow);
  }
  .web-row {
    position: absolute;
    left: 0; right: 0; top: 464px;
    height: 40px;
  }
  .web-address {
    position: absolute;
    left: 0; right: 0; top: 2px;
    text-align: center;
    font-size: 23px;
    color: var(--ink);
  }
  .social {
    position: absolute;
    top: 8px;
    display: flex;
    align-items: center;
    gap: 5px;
    font-size: 13px;
    font-weight: 700;
    color: var(--navy);
  }
  .social .mark { width: 14px; height: 14px; background: var(--navy); border-radius: 2px; }
  .social-chatterly { left: 150px; }
  .social-blipster { left: 596px; }

  .benefits-heading {
    position: absolute;
    left: 36px; top: 108px;
    font-size: 18.5px;
    font-weight: 700;
    color: var(--orange);
  }
  .benefits-list {
    position: absolute;
    left: 36px; top: 146px;
    width: 660px;
    list-style: none;
    color: var(--green-dark);
    font-size: 17.5px;
    line-height: 26px;
  }
  .benefits-list li { display: flex; margin-bottom: 17px; }
  .benefits-list .letter { width: 34px; flex: none; }

  .faded-shoe {
    position: absolute;
    width: 118px; height: 84px;
    border-radius: 20px;
    border: 2px solid #c9e3c7;
    opacity: 0.45;
  }
  .faded-shoe.light { background: linear-gradient(160deg, #f2f2f2, var(--shoe-light) 55%, #b9a58c); }
  .faded-shoe.dark { background: linear-gradient(160deg, #f4f4f2, #6b6b5a 60%, #efe29a); }

  .member-fields {
    position: absolute;
    left: 38px; top: 464px;
    display: flex;
    gap: 22px;
    font-size: 18px;
    font-weight: 700;
  }
  .member-field { display: flex; align-items: flex-end; gap: 4px; }
  .member-field .line { display: inline-block; height: 1px; background: var(--navy); margin-bottom: 5px; }
  .member-name { color: var(--green-dark); }
  .member-name .line { width: 300px; }
  .member-id { color: var(--orange); }
  .member-id .line { width: 160px; }
</style>
</head>
<body>

<section class="card card-front" aria-label="Card front">
  <svg class="card-art" width="810" height="509" viewBox="0 0 810 509" aria-hidden="true">
    <defs>
      <linearGradient id="front-green" x1="0" y1="0" x2="1" y2="0">
        <stop offset="0" stop-color="#1f6b2a"/>
        <stop offset="0.55" stop-color="#2e8b37"/>
        <stop offset="1" stop-color="#1f6b2a"/>
      </linearGradient>
    </defs>
    <rect width="810" height="462" fill="url(#front-green)"/>
    <path d="M0 128 Q260 -10 810 86 L810 270 Q520 330 360 408 Q140 380 0 300 Z" fill="#ffffff"/>
    <path d="M0 150 Q260 -2 810 62" fill="none" stroke="var(--orange)" stroke-width="5"/>
    <path d="M0 270 Q160 380 360 392 Q560 360 810 250" fill="none" stroke="var(--orange)" stroke-width="4"/>
    <rect y="462" width="810" height="47" fill="#ffffff"/>
  </svg>

  <div class="brand-name">Trodza</div>

  <div class="shoe-photo light" style="left:59px; top:252px; width:145px; height:103px;" role="img" aria-label="Photo of a white and red Velm sneaker"></div>
  <div class="shoe-photo light" style="left:306px; top:300px; width:144px; height:106px;" role="img" aria-label="Photo of a white Brenvo sneaker with green stripes"></div>
  <div class="shoe-photo dark" style="left:566px; top:230px; width:144px; height:103px;" role="img" aria-label="Photo of a black and yellow Quorra sneaker"></div>

  <div class="discount-badge" style="left:26px; top:203px;"><span class="pct">24%</span><span class="word">Discount</span></div>
  <div class="discount-badge" style="left:267px; top:267px;"><span class="pct">24%</span><span class="word">Discount</span></div>
  <div class="discount-badge" style="left:707px; top:203px;"><span class="pct">24%</span><span class="word">Discount</span></div>

  <div class="club-title">Trodza VIP Circle 9</div>
  <div class="web-row">
    <div class="social social-chatterly"><span class="mark"></span>Chatterly</div>
    <div class="web-address">www.trodzashop.com</div>
    <div class="social social-blipster"><span class="mark"></span>blipster</div>
  </div>
</section>

<section class="card card-back" aria-label="Card back">
  <svg class="card-art" width="810" height="509" viewBox="0 0 810 509" aria-hidden="true">
    <defs>
      <linearGradient id="back-green" x1="0" y1="0" x2="1" y2="0">
        <stop offset="0" stop-color="#1f6b2a"/>
        <stop offset="0.5" stop-color="#3f9a40"/>
        <stop offset="1" stop-color="#1f6b2a"/>
      </linearGradient>
    </defs>
    <path d="M0 0 H810 V80 Q420 -10 0 104 Z" fill="url(#back-green)"/>
    <path d="M0 112 Q420 0 810 100" fill="none" stroke="var(--orange)" stroke-width="5"/>
  </svg>

  <p class="benefits-heading">The TRODZA Member Program entitles Members to the following benefits:</p>
  <ul class="benefits-list">
    <li><span class="letter">a.</span><span>20% OFF your entire first purchase after you sign up (Limited Time Offer).<br>Certain items are excluded from this offer. Please see stores for details.</span></li>
    <li><span class="letter">b.</span><span>10% OFF every purchase while being a member.<br>Certain items are excluded from this offer. Please see stores for details.</span></li>
    <li><span class="letter">c.</span><span>Additional 10% OFF and FREE SHIPPING when an item is out of stock<br>in store but can be shipped to you from another location.</span></li>
    <li><span class="letter">d.</span><span>Eligible to purchase exclusive items offered to members only.<br>Purchasing of exclusive items is limited to 1 item per member per 30 days.<br>Please see stores for details.</span></li>
  </ul>

  <div class="faded-shoe light" style="left:670px; top:156px;" role="img" aria-label="Faded photo of a Velm sneaker"></div>
  <div class="faded-shoe light" style="left:676px; top:252px;" role="img" aria-label="Faded photo of a Brenvo sneaker"></div>
  <div class="faded-shoe dark" style="left:676px; top:354px;" role="img" aria-label="Faded photo of a Quorra sneaker"></div>

  <div class="member-fields">
    <div class="member-field member-name">Member Name :<span class="line"></span></div>
    <div class="member-field member-id">Member ID :<span class="line"></span></div>
  </div>
</section>

</body>
</html>
```